Iconic website for iconic products

We want a website which will stand out, which will reflect that we are offering cutting edge solutions, breaking the mould. The website must be very search engine friendly, to drive traffic from all around the world, and also sticky, so that they explore what we have to offer, and hopefully buy from us.

We have launched a portfolio of products in the field of 3D, which are highly accessible. They are accessible in their openness, their ease of use and their ultra low cost. We are providing everyone everywhere the opportunity to engage in 3D design and to produce physical 3D models as outputs from their designs. This technology is ground breaking and world changing.

The website will need to be easy for us to maintain and grow, easy for our customers and prospects to use, easy to find.

We will need to integrate a blog, and provide eCommerce capability. We will also be looking to add a forum, which we will need to monitor and maintain, so that our customers can connect with one another, share best practice, offer solutions to problems, and generate value for one another, while reducing our after-sales support burden.

We will also need to set up page templates for our key customers to show what they have done with our products so that others can share the experience.

Target Market(s)

We have a number of distinct markets.
Education:
Primary (5-11) schools
Secondary (11-18) schools
Colleges (16-19)
Universities
Creative designers and designer-makers
Industrial companies; any that are involved in design, in manufacture, in marketing
Animation, games and virtual world organisations
Hobbyists

Industry/Entity Type

Sales

Requirements
Must have
• Iconic design
• Ease of maintenance and future build
• Blog
• eCommerce
• Forum
• Chirper
• When people enquire, people must fill in forms to download information, and we must capture that information on a database.
• We also need a secure log in area for distributors and resellers to access for confidential information.
Nice to have
• An updated logo to match the website
Should not have
• Old fashioned design
• Bricks and mortar feel

```html
<!DOCTYPE html>
<html lang="en">
<head>
<meta charset="utf-8">
<title>Nova3 Labs – Low cost 3D technologies</title>
<link href="https://fonts.googleapis.com/css2?family=Share+Tech+Mono&family=PT+Serif&family=Open+Sans:wght@400;600;700&display=swap" rel="stylesheet">
<style>
:root{
  --ink:#222;
  --muted:#444;
  --page:#e9e9e9;
  --panel:#fff;
  --well:#dcdcdc;
  --line:#c8c8c8;
  --red:#c9292b;
  --red-dark:#a31f22;
  --cyan:#19e0f2;
  --price:#a11414;
  --link:#1a55c9;
}
*{margin:0;padding:0;box-sizing:border-box}
html,body{width:906px;height:1200px;overflow:hidden}
body{background:var(--page);font-family:"Open Sans",Arial,sans-serif;color:var(--ink);position:relative;font-size:9px}
.abs{position:absolute}

/* header */
.hero{left:0;top:0;width:906px;height:313px;background:radial-gradient(ellipse 360px 200px at 470px 210px,#4fe3ee 0%,#21b4c4 40%,#0b5964 75%,#050b0d 100%);overflow:hidden}
.hero-top{left:0;top:0;width:906px;height:80px;background:linear-gradient(#000 0%,rgba(0,0,0,.85) 55%,rgba(0,0,0,0))}
.brand{left:56px;top:26px;display:flex;align-items:center;gap:8px;color:#fff;font-weight:700;font-size:18px;letter-spacing:.5px}
.brand-dot{width:22px;height:22px;border-radius:50%;background:var(--red)}
.nav{right:56px;top:28px;display:flex;gap:22px;align-items:center}
.nav a{color:#e9f4f6;text-decoration:none;font-family:"Share Tech Mono",monospace;font-size:16px;letter-spacing:1px}
.nav a.current{background:#2a2a2a;border:1px solid #555;border-radius:5px;padding:3px 17px;position:relative}
.nav a.current:after{content:"";position:absolute;left:50%;bottom:-7px;margin-left:-6px;border:6px solid transparent;border-top-color:#2a2a2a;border-bottom:0}
.tagline{left:214px;top:102px;color:#cfe9ee;font-family:"Share Tech Mono",monospace;font-size:22px;line-height:28px;letter-spacing:.5px}
.tagline b{font-weight:400;color:#111;font-size:26px}
.art-person{left:40px;top:110px;width:310px;height:210px;background:linear-gradient(135deg,#e8e8e8,#9a9a9a);opacity:.85;border-radius:90px 40px 10px 10px}
.art-robot{left:720px;top:100px;width:130px;height:225px;background:linear-gradient(160deg,#f2f2f2,#7a7f86);border-radius:50px 50px 20px 20px}
.band{left:0;top:313px;width:906px;height:35px;background:linear-gradient(#c6c6c6,#b9b9b9)}
.social{left:609px;top:318px;display:flex;gap:3px}
.social span{width:26px;height:26px;border-radius:4px;display:block}

/* page */
.sheet{left:40px;top:348px;width:826px;height:774px;background:var(--panel);border:1px solid #d2d2d2;border-top:0}
.intro{left:50px;top:364px;width:535px;font-size:9.5px;line-height:14.9px;color:var(--muted)}
.intro .lead{font-family:"PT Serif",serif;font-size:15px;color:#222}

.login{left:594px;top:360px;width:262px;height:127px;background:radial-gradient(ellipse at 50% 40%,#d8393b,var(--red-dark));border:3px solid #b82326;color:#f3d5d5}
.login h2{position:absolute;left:20px;top:6px;font-family:"PT Serif",serif;font-weight:400;font-size:20px;line-height:26px;color:#fff}
.login label{position:absolute;font-size:9px;line-height:12px;letter-spacing:.5px;white-space:nowrap}
.login .field{position:absolute;left:71px;width:170px;height:16px;background:#d43436;border:1px solid #e26364}
.login .lock{position:absolute;left:51px;top:85px}
.login .check{position:absolute;left:63px;top:87px;width:9px;height:9px;background:#ddd}
.login .btn{position:absolute;left:167px;top:83px;width:70px;height:21px;border-radius:10px;background:linear-gradient(#3a3a3a,#111);color:#fff;font-family:"Share Tech Mono",monospace;font-size:15px;text-align:center;line-height:21px;letter-spacing:1px}

.show{left:50px;top:496px;width:535px;height:191px;background:#dcdcdc;border:1px solid var(--line)}
.show h3{position:absolute;left:9px;top:8px;font-family:"PT Serif",serif;font-weight:400;font-size:15px;line-height:16px;color:var(--red)}
.quote{position:absolute;left:13px;width:235px;height:43px;background:var(--cyan);border-radius:5px;padding:4px 6px 0 48px;font-size:8.3px;line-height:11px;color:#134}
.quote .ava{position:absolute;left:6px;top:5px;width:33px;height:33px;background:#2d3b44;border:1px solid #fff}
.quote b{display:block;font-size:9.5px;color:#111}
.quote i{position:absolute;right:6px;bottom:3px;font-style:normal;text-decoration:underline;color:var(--link)}
.video{position:absolute;left:256px;top:11px;width:268px;height:150px;border:1px solid #aaa;background:#fff}
.video .frame{position:absolute;left:0;top:0;width:266px;height:135px;background:linear-gradient(120deg,#2c4f86 0%,#5d7fb3 45%,#b89a74 70%,#d9d2c8 100%)}
.video .bar{position:absolute;left:0;bottom:0;width:266px;height:13px;background:#e5e5e5;border-top:1px solid #bbb}
.video .track{position:absolute;left:84px;top:5px;width:140px;height:3px;background:#aaa}
.video .track:before{content:"";position:absolute;left:0;top:0;width:8px;height:3px;background:var(--red)}
.browse{position:absolute;right:13px;top:170px;font-weight:700;font-size:9.5px;line-height:12px;color:var(--red)}

.side-head{left:594px;top:497px;width:262px;height:34px;background:linear-gradient(#111,#000);color:#fff;font-family:"PT Serif",serif;font-size:20px;padding:3px 0 0 11px}
.bird{position:absolute;right:10px;top:7px;width:18px;height:18px;border-radius:50%;background:#49a9e0}
.tweet{left:604px;width:245px;font-size:8.5px;line-height:15px;color:#111;padding-left:50px}
.tweet .ava{position:absolute;left:0;top:2px;width:39px;height:39px}
.tweet a{color:var(--link);text-decoration:underline}
.pill{position:absolute;height:15px;border-radius:8px;background:linear-gradient(#d6d6d6,#a9a9a9);font-size:9px;line-height:13px;text-align:center;color:#333;border:1px solid #999;white-space:nowrap}

.bar-head{height:34px;background:linear-gradient(#151515,#000);color:#fff;font-family:"PT Serif",serif;font-size:20px;padding:3px 0 0 13px}
.well{background:var(--well);border:1px solid var(--line)}
.product h4{position:absolute;left:16px;font-family:"PT Serif",serif;font-weight:400;font-size:20px;line-height:26px;color:#111}
.price{position:absolute;left:438px;width:78px;height:40px;border:1px solid #999;border-radius:10px;background:linear-gradient(#fff,#cfcfcf);text-align:center;font-size:8.5px;line-height:11px;color:#333;padding-top:4px}
.price b{display:block;font-family:"Share Tech Mono",monospace;font-weight:400;color:var(--price);font-size:20px;line-height:20px;letter-spacing:1px}
.shot{position:absolute;left:18px;width:198px;height:83px;border:3px solid #fff;box-shadow:0 1px 3px rgba(0,0,0,.35)}
.blurb{position:absolute;left:230px;width:285px;font-size:7.8px;line-height:11.6px;color:#333}
.divider{position:absolute;left:12px;width:510px;height:1px;background:#c4c4c4}
.post{position:absolute;left:12px;width:235px;font-size:8px;line-height:11.7px;color:#333;padding-left:20px}
.post:before{content:"";position:absolute;left:3px;top:1px;border:5px solid transparent;border-left:7px solid #aaa}
.post b{display:block;color:#111;font-size:8.6px}
.post em{display:block;font-style:normal;color:var(--red);margin-bottom:10px}

.footer{left:0;top:1142px;width:906px;height:58px;background:#141414;color:#ddd;font-size:8.5px}
.footer .links{position:absolute;left:328px;top:17px;line-height:12px}
.footer .brand-mini{position:absolute;left:252px;top:34px;display:flex;align-items:center;gap:5px;font-weight:700;font-size:10px;line-height:14px;color:#bbb}
.footer .brand-mini span{width:12px;height:12px;border-radius:50%;border:1px solid #bbb;display:block}
.footer .contact{position:absolute;left:408px;top:35px;line-height:12px}
</style>
</head>
<body>

<header class="abs hero">
  <div class="abs art-person" role="img" aria-label="Illustration of a figure working at a laptop projecting a 3D model"></div>
  <div class="abs art-robot" role="img" aria-label="Illustration of a white robot model scanned in a teal light beam"></div>
  <div class="abs hero-top"></div>
  <div class="abs brand"><span class="brand-dot"></span>NOVA3 LABS</div>
  <nav class="abs nav">
    <a class="current" href="#">HOME</a>
    <a href="#">JOIN NOVA3</a>
    <a href="#">PRODUCTS</a>
    <a href="#">BLOG</a>
    <a href="#">FORUM</a>
    <a href="#">CONTACT</a>
  </nav>
  <p class="abs tagline">Incredibly low cost <b>3D TECHNOLOGIES</b><br>for designing &amp; producing <b>3D MODELS</b></p>
</header>
<div class="abs band"></div>
<div class="abs social" aria-label="Social links">
  <span style="background:#2a5fb8"></span><span style="background:#ef8a1c"></span><span style="background:#2f55a4"></span><span style="background:#2c8fcf"></span>
</div>

<main class="abs sheet"></main>

<p class="abs intro"><span class="lead">Nova3 Labs</span> offers schools and colleges cutting edge products and solutions in the fields of 3D modelling and printing, at incredibly low prices. Ideal for teaching and learning. Lorem ipsum dolor sit amet, consectetur adipiscing elit. Integer sapien quam, accumsan quis auctor non, dapibus ut dolor. Nam sem tellus, consectetur in imperdiet et, feugiat eu sem. Donec eget leo accumsan odio convallis vulputate. Vivamus erat massa, fringilla eu consectetur ac, cursus sed neque.Lorem ipsum dolor sit amet, consectetur adipiscing elit. Proin tempus pulvinar sem vel pharetra. Sed suscipit malesuada tortor, a varius nulla auctor eu. Sed nec velit lectus, id consectetur metus. Aenean eu interdum nisi.</p>

<section class="abs login">
  <h2>Member Login</h2>
  <label style="left:22px;top:41px">Username</label><div class="field" style="top:38px"></div>
  <label style="left:26px;top:61px">Password</label><div class="field" style="top:58px"></div>
  <svg class="lock" width="9" height="11" viewBox="0 0 9 11"><rect x="1" y="5" width="7" height="6" fill="#e8c26b"/><path d="M2.5 5V3.2a2 2 0 0 1 4 0V5" stroke="#ddd" fill="none"/></svg>
  <div class="check"></div>
  <label style="left:77px;top:85px">Login as Reseller</label>
  <label style="left:77px;top:101px">Forgot Password?</label>
  <div class="btn">LOGIN</div>
</section>

<section class="abs show">
  <h3>See what our customers really did<br>with our products</h3>
  <div class="quote" style="top:61px"><span class="ava" role="img" aria-label="Customer photo"></span><b>Mira Santos</b>I purchased Chromaform 3D Creative solution and I did some incredibly<i>Visit</i></div>
  <div class="quote" style="top:119px"><span class="ava" role="img" aria-label="Customer avatar"></span><b>Tomas Reyel</b>I purchased Chromaform 3D Creative solution and I did some incredibly<i>Visit</i></div>
  <div class="video">
    <div class="frame" role="img" aria-label="Video still of a customer assembling a 3D printed helmet beside a screen showing a model"></div>
    <div class="bar">
      <svg style="position:absolute;left:4px;top:3px" width="60" height="7"><rect x="0" y="0" width="2" height="7" fill="#333"/><rect x="4" y="0" width="2" height="7" fill="#333"/><path d="M14 2h2l3-2v7l-3-2h-2z" fill="#333"/><text x="30" y="6" font-size="5.5" fill="#333" font-family="Arial">0:04 / 1:51</text></svg>
      <div class="track"></div>
      <svg style="position:absolute;right:4px;top:3px" width="40" height="7"><text x="0" y="6" font-size="5.5" fill="#333" font-family="Arial">360p</text><rect x="20" y="1" width="5" height="5" fill="none" stroke="#333"/><rect x="30" y="0" width="9" height="7" rx="1" fill="#333"/></svg>
    </div>
  </div>
  <span class="browse">Browse more projects &gt;&gt;</span>
</section>

<div class="abs side-head">Nova3 on Chirper<span class="bird"></span></div>
<div class="abs tweet" style="top:545px"><span class="ava" style="background:#2e8a5c" role="img" aria-label="Account avatar"></span><a>PixelKiwi</a>: Create Your Own Custom Avatar on Chromaform software(expand)<br>1 day ago via mobile web · <a>Reply</a> · <a>View Post</a></div>
<div class="abs tweet" style="top:611px"><span class="ava" style="background:#6b4a3a" role="img" aria-label="Account photo"></span><a>PixelKiwi</a>: Create Your Own Custom Avatar on Chromaform software(expand)<br>1 day ago via mobile web · <a>Reply</a> · <a>View Post</a></div>
<span class="pill" style="left:724px;top:671px;width:54px">View All</span>
<span class="pill" style="left:788px;top:671px;width:58px">Share it</span>

<div class="abs bar-head" style="left:50px;top:696px;width:535px">Our Iconic Products<span class="pill" style="left:421px;top:9px;width:104px;background:linear-gradient(#555,#2a2a2a);color:#eee;border-color:#666;font-family:'Open Sans',sans-serif">View All Products</span></div>
<section class="abs well" style="left:50px;top:737px;width:535px;height:369px">
  <div class="product">
    <h4 style="top:21px">Chromaform 3D Creative Package</h4>
    <div class="price" style="top:12px">Starting from<b>£350</b></div>
    <div class="shot" style="top:61px;background:linear-gradient(135deg,#6e8fb8,#8aa4c6 60%,#4a6aa8)" role="img" aria-label="Rendered 3D models: a spiral ring and a folded blue shape"></div>
    <p class="blurb" style="top:64px">Lorem ipsum dolor sit amet, consectetur adipisicing elit, sed do eiusmod tempor incididunt ut labore et dolore magna aliqua. Ut enim ad minim veniam, quis nostrud exercitation ullamco laboris nisi ut aliquip ex ea commodo consequat.</p>
    <span class="pill" style="left:386px;top:132px;width:59px">Explore</span>
    <span class="pill" style="left:453px;top:132px;width:59px">Buy Now</span>
  </div>
  <div class="divider" style="top:165px"></div>
  <div class="product">
    <h4 style="top:186px">Orbis 3D Laser Scanner</h4>
    <div class="price" style="top:177px">Starting from<b>£320</b></div>
    <div class="shot" style="top:231px;left:20px;background:linear-gradient(120deg,#3f6aa6,#8fa9c8 55%,#c8c2b0)" role="img" aria-label="Laser scanner projecting a beam onto a small figurine"></div>
    <p class="blurb" style="top:229px">Lorem ipsum dolor sit amet, consectetur adipisicing elit, sed do eiusmod tempor incididunt ut labore et dolore magna aliqua. Ut enim ad minim veniam, quis nostrud exercitation ullamco laboris nisi ut aliquip ex ea commodo consequat.</p>
    <span class="pill" style="left:386px;top:297px;width:59px">Explore</span>
    <span class="pill" style="left:453px;top:297px;width:59px">Buy Now</span>
  </div>
</section>

<div class="abs bar-head" style="left:594px;top:696px;width:262px">Recent Blog Posts</div>
<section class="abs well" style="left:594px;top:737px;width:262px;height:369px">
  <div class="post" style="top:13px"><b>2 of Byte Harbour's useful tools move to 2.0</b><em>July 17, 2010 – 8:48 am</em>It's probably been a busy week or two over in the UK for somebody as Byte Harbour...[ ]</div>
  <div class="divider" style="top:87px;width:238px"></div>
  <div class="post" style="top:104px"><b>Norvane's 3D Plan? We Can Fix It in Post</b><em>July 14, 2010 – 1:57 pm</em>Ever wonder why Kelvar has so far had free reign to talk up an all-in-one stereo 3D camcorder[...]</div>
  <div class="divider" style="top:176px;width:238px"></div>
  <div class="post" style="top:193px"><b>Critics Slam 3D in Sky Warden</b><em>July 6, 2010 – 10:13 am</em>The critics got their knives out for The Sky Warden last week — the film earned an abysmal [...]</div>
  <div class="post" style="top:272px"><b>Useful Tool for EditPro Network Admins</b><em>July 12, 2010 – 10:43 am</em>Cutline Studio has recently released a new tool that adds additional functionality to one [...]</div>
  <span class="pill" style="left:193px;top:340px;width:60px">View Blog</span>
</section>

<footer class="abs footer">
  <div class="links">About Us | Forum | Blog | Products | Privacy | AUP | Contact Us</div>
  <div class="brand-mini"><span></span>NOVA3 LABS LTD</div>
  <div class="contact">
    <svg width="9" height="9" viewBox="0 0 9 9" style="vertical-align:-1px;margin-right:4px"><rect x="0" y="0" width="9" height="9" rx="1.5" fill="#ddd"/><path d="M2.5 2c.5 2 2.5 4 4.5 4.5l.3-1-1.3-.6-.6.6c-.8-.4-1.5-1.1-1.9-1.9l.6-.6L3.5 1.7z" fill="#141414"/></svg>0700 555 0142 / 07700 900 318 ,&nbsp; info@nova3labs.example
  </div>
</footer>

</body>
</html>
```